PowerPoint Design Project

Kestrel Estate Group is a Melbourne based property development management company. We provide a comprehensive range of development management services to a select group of listed developers, private landowners, overseas investors and development partners and institutional clients. Our website provides additional information about the company:
http://www.kestreleg.com.au
We are looking for a versatile powerpoint design that can be used across a wide variety of presentations including; pitch documents, client reports, Information memorandums, and downloadable credential packs etc. We have attached a good example document.
Updates

Industry/Entity Type

It Company

Requirements
Must have
• The design should have the following slides as a minimum: Intro Page, transition slides, profile slides, slides for graphics,

```html
<!DOCTYPE html>
<html lang="en">
<head>
<meta charset="utf-8">
<title>Kestrel Estate Group – Presentation Template</title>
<link href="https://fonts.googleapis.com/css2?family=Source+Sans+3:ital,wght@0,400;0,600;0,700;1,700&family=Arimo:ital,wght@0,400;0,700;1,700&display=swap" rel="stylesheet">
<style>
  :root{
    --board:#e9e4dc;
    --paper:#ffffff;
    --ink:#111111;
    --body:#5b5b5b;
    --band:#58585a;
    --band-line:#0d0d0d;
    --cyl-top:#2a2a2a;
    --cyl-side:#9a9a9a;
    --connector:#b5b5b5;
  }
  *{box-sizing:border-box;margin:0;padding:0}
  html,body{width:1200px;height:443px;overflow:hidden;background:var(--board)}
  body{font-family:"Source Sans 3",sans-serif;color:var(--ink);position:relative}
  .slide{position:absolute;width:264px;height:196px;background:var(--paper);overflow:hidden;box-shadow:0 1px 3px rgba(0,0,0,.18)}
  .row-top{top:14px}.row-bottom{top:230px}
  .col-1{left:22px}.col-2{left:320px}.col-3{left:600px}.col-4{left:898px}
  .footer{position:absolute;left:0;bottom:0;width:264px;height:38px}
  .footer svg{display:block;width:100%;height:100%}
  .footer-url{position:absolute;right:7px;bottom:5px;font-size:6.5px;color:#fff;letter-spacing:.2px}
  .slide-heading{position:absolute;left:15px;top:11px;font-size:11px;font-weight:400;text-transform:uppercase;letter-spacing:.1px}
  .copy{position:absolute;font-size:5.2px;line-height:7.2px;color:var(--body)}
  .photo{position:absolute;border-radius:7px}
  .brand{position:absolute;display:flex;align-items:center;gap:4px;font-weight:700;font-size:13.5px;letter-spacing:.4px;color:var(--ink);text-transform:uppercase;white-space:nowrap}
  .brand-mark{width:9px;height:9px;background:var(--ink)}
  .cover-title{position:absolute;left:0;width:264px;top:128px;text-align:center;font-family:Arimo,sans-serif;font-size:14.5px;font-weight:400}
  .intro-photos .photo{top:106px;width:52px;height:46px}
  .graphic{position:absolute;left:0;top:0}
  .table-bg{position:absolute;inset:0;background:linear-gradient(120deg,#ece9ef 0%,#e6e2e8 40%,#f1eeee 70%,#ddd8dc 100%)}
  .table-cell{position:absolute;width:116px}
  .table-cell h4{font-size:6.3px;font-weight:600;color:#333;line-height:8px}
  .table-cell p{font-size:6.3px;line-height:8px;color:#333}
  .part-label{position:absolute;left:0;width:264px;top:61px;text-align:center;font-family:Arimo,sans-serif;font-weight:700;font-size:14px}
  .transition-copy{left:44px;width:176px;top:90px;text-align:center}
  .profile-photo{position:absolute;left:13px;top:56px;width:121px;height:91px;border:1px solid #444;background:linear-gradient(180deg,#e8e8e8 0%,#cfc7c0 45%,#2b2b2e 100%)}
  .profile-copy{left:148px;top:52px;width:104px;text-align:justify}
  .thanks{position:absolute;left:0;width:264px;top:108px;text-align:center;font-family:Arimo,sans-serif;font-style:italic;font-weight:700;font-size:12.5px;line-height:15px}
</style>
</head>
<body>

<!-- Cover -->
<section class="slide row-top col-1">
  <div class="brand" style="left:40px;top:78px"><span class="brand-mark"></span>Kestrel Estate Group</div>
  <h1 class="cover-title">Title of Presentation</h1>
  <div class="footer"><svg viewBox="0 0 264 38" preserveAspectRatio="none"><path d="M0 22 C70 8 150 30 264 12 L264 38 L0 38Z" fill="var(--band)"/><path d="M0 20 C70 6 150 28 264 10" fill="none" stroke="var(--band-line)" stroke-width="2.4"/><path d="M0 16 C80 4 160 22 264 6" fill="none" stroke="#cfcfcf" stroke-width=".6"/></svg><span class="footer-url">www.kestreleg.com.au</span></div>
</section>

<!-- Intro -->
<section class="slide row-top col-2 intro-photos">
  <h2 class="slide-heading">Intro Page</h2>
  <p class="copy" style="left:15px;top:38px;width:235px">Lorem ipsum dolor sit amet, consectetuer adipiscing elit, sed diam nonummy nibh euismod tincidunt ut laoreet dolore magna aliquam erat volutpat. Ut wisi enim ad minim veniam, quis nostrud exerci tation ullamcorper suscipit lobortis nisl ut aliquip ex ea commodo consequat. Duis autem vel eum iriure dolor in hendrerit in vulputate velit esse molestie consequat, vel illum dolore eu feugiat nulla facilisis.</p>
  <div class="photo" style="left:14px;background:linear-gradient(135deg,#c9262a,#f2f2f2 60%,#555)" role="img" aria-label="Red staircase in a modern interior"></div>
  <div class="photo" style="left:76px;background:linear-gradient(135deg,#3c2a55,#c8962f 60%,#2a2030)" role="img" aria-label="Building facade lit at night"></div>
  <div class="photo" style="left:138px;background:linear-gradient(180deg,#f2f2f0,#cfcac2 60%,#e8e6e2)" role="img" aria-label="Bright open-plan interior"></div>
  <div class="photo" style="left:200px;background:linear-gradient(135deg,#3a3a3a,#b8b8b8 55%,#2a2a2a)" role="img" aria-label="Commercial building with signage"></div>
  <div class="footer"><svg viewBox="0 0 264 38" preserveAspectRatio="none"><path d="M0 22 C70 8 150 30 264 12 L264 38 L0 38Z" fill="var(--band)"/><path d="M0 20 C70 6 150 28 264 10" fill="none" stroke="var(--band-line)" stroke-width="2.4"/><path d="M0 16 C80 4 160 22 264 6" fill="none" stroke="#cfcfcf" stroke-width=".6"/></svg><span class="footer-url">www.kestreleg.com.au</span></div>
</section>

<!-- Graphics -->
<section class="slide row-top col-3">
  <h2 class="slide-heading">Slides for Graphics</h2>
  <svg class="graphic" width="264" height="196" viewBox="0 0 264 196" font-family="Source Sans 3, sans-serif">
    <defs>
      <linearGradient id="cylSide" x1="0" x2="1"><stop offset="0" stop-color="#7a7a7a"/><stop offset=".45" stop-color="#c4c4c4"/><stop offset="1" stop-color="#6e6e6e"/></linearGradient>
      <g id="cylinder">
        <rect x="0" y="4" width="32" height="24" fill="url(#cylSide)"/>
        <ellipse cx="16" cy="28" rx="16" ry="4" fill="#777"/>
        <ellipse cx="16" cy="4" rx="16" ry="4" fill="var(--cyl-top)"/>
        <text x="16" y="19.5" font-size="4.6" font-weight="700" fill="#fff" text-anchor="middle">Lorem</text>
      </g>
      <g id="label">
        <rect x="0" y="0" width="42" height="18" rx="3" fill="#000"/>
        <text x="21" y="11" font-size="4.8" font-weight="700" fill="#fff" text-anchor="middle">Lorem ipsum</text>
      </g>
    </defs>
    <g stroke="var(--connector)" stroke-width=".6" fill="none">
      <path d="M38 60 H32 V113 H44 M32 81 H44"/>
      <path d="M88 60 H82 V145 H94 M82 81 H94 M82 113 H94"/>
      <path d="M138 60 H132 V145 H144 M132 81 H144 M132 113 H144"/>
      <path d="M188 60 H182 V145 H194 M182 81 H194 M182 113 H194"/>
    </g>
    <use href="#label" x="38" y="42"/><use href="#label" x="88" y="42"/><use href="#label" x="138" y="42"/><use href="#label" x="188" y="42"/>
    <use href="#cylinder" x="44" y="66"/><use href="#cylinder" x="44" y="98"/>
    <use href="#cylinder" x="94" y="66"/><use href="#cylinder" x="94" y="98"/><use href="#cylinder" x="94" y="130"/>
    <use href="#cylinder" x="144" y="66"/><use href="#cylinder" x="144" y="98"/><use href="#cylinder" x="144" y="130"/>
    <use href="#cylinder" x="194" y="66"/><use href="#cylinder" x="194" y="98"/><use href="#cylinder" x="194" y="130"/>
  </svg>
  <div class="footer"><svg viewBox="0 0 264 38" preserveAspectRatio="none"><path d="M0 22 C70 8 150 30 264 12 L264 38 L0 38Z" fill="var(--band)"/><path d="M0 20 C70 6 150 28 264 10" fill="none" stroke="var(--band-line)" stroke-width="2.4"/><path d="M0 16 C80 4 160 22 264 6" fill="none" stroke="#cfcfcf" stroke-width=".6"/></svg><span class="footer-url">www.kestreleg.com.au</span></div>
</section>

<!-- Table -->
<section class="slide row-top col-4">
  <div class="table-bg" role="img" aria-label="Faded photo of a building interior behind the table"></div>
  <h2 class="slide-heading">Slides for Table</h2>
  <div class="table-cell" style="left:12px;top:43px"><h4>Sub Title-1</h4><p>Lorem ipsum dolor sit amet, etuer.Lorem ipsum dolor sit amet, etuer.Lorem ipsum dolor sit amet, etuer.Lorem ipsum dolor</p></div>
  <div class="table-cell" style="left:142px;top:43px"><h4>Sub Title-1</h4><p>Lorem ipsum dolor sit amet, etuer.Lorem ipsum dolor sit amet, etuer.Lorem ipsum dolor sit amet, etuer.Lorem ipsum dolor</p></div>
  <div class="table-cell" style="left:12px;top:90px"><h4>Sub Title-2</h4><p>Lorem ipsum dolor sit amet, etuer.Lorem ipsum dolor sit amet, etuer.Lorem ipsum dolor sit amet, etuer.Lorem ipsum dolor</p></div>
  <div class="table-cell" style="left:142px;top:90px"><h4>Sub Title-2</h4><p>Lorem ipsum dolor sit amet, etuer.Lorem ipsum dolor sit amet, etuer.Lorem ipsum dolor sit amet, etuer.Lorem ipsum dolor</p></div>
  <div class="table-cell" style="left:12px;top:136px"><h4>Sub Title-3</h4><p>Lorem ipsum dolor sit amet, etuer.Lorem ipsum dolor sit amet, etuer.Lorem ipsum dolor sit amet, etuer.Lorem ipsum dolor</p></div>
  <div class="table-cell" style="left:142px;top:136px"><h4>Sub Title-3</h4><p>Lorem ipsum dolor sit amet, etuer.Lorem ipsum dolor sit amet, etuer.Lorem ipsum dolor sit amet, etuer.Lorem ipsum dolor</p></div>
  <div class="footer"><svg viewBox="0 0 264 38" preserveAspectRatio="none"><path d="M0 22 C70 8 150 30 264 12 L264 38 L0 38Z" fill="var(--band)"/><path d="M0 20 C70 6 150 28 264 10" fill="none" stroke="var(--band-line)" stroke-width="2.4"/><path d="M0 16 C80 4 160 22 264 6" fill="none" stroke="#cfcfcf" stroke-width=".6"/></svg><span class="footer-url">www.kestreleg.com.au</span></div>
</section>

<!-- Transition -->
<section class="slide row-bottom col-1">
  <h2 class="slide-heading">Transition Slides</h2>
  <p class="part-label">PART 3</p>
  <p class="copy transition-copy">Orem ipsum dolor sit amet, consectetuer adipiscing elit, sed diam nonummy nibh euismod tincidunt ut laoreet dolore magna aliquam erat volutpat. Ut wisi enim ad minim veniam, quis nostrud exerci tation ullamcorper suscipit lobortis nisl ut aliquip ex ea commodo consequat. Duis autem vel eum iriure dolor in hendrerit in</p>
  <div class="footer"><svg viewBox="0 0 264 38" preserveAspectRatio="none"><path d="M0 22 C70 8 150 30 264 12 L264 38 L0 38Z" fill="var(--band)"/><path d="M0 20 C70 6 150 28 264 10" fill="none" stroke="var(--band-line)" stroke-width="2.4"/><path d="M0 16 C80 4 160 22 264 6" fill="none" stroke="#cfcfcf" stroke-width=".6"/></svg><span class="footer-url">www.kestreleg.com.au</span></div>
</section>

<!-- Profile -->
<section class="slide row-bottom col-2">
  <h2 class="slide-heading">Profile Slides</h2>
  <div class="profile-photo" role="img" aria-label="Portrait photo of three smiling business people"></div>
  <p class="copy profile-copy">Lorem ipsum dolor sit amet, consectetuer adipiscing elit, sed diam nonummy nibh euismod tincidunt ut laoreet dolore magna aliquam erat volutpat. Ut wisi enim ad minim veniam, quis nostrud exerci tation ullamcorper suscipit lobortis nisl ut aliquip ex ea commodo consequat. Duis autem vel eum iri. Lorem ipsum dolor sit amet, consectetuer adipiscing elit, sed diam nonummy nibh euismod</p>
  <div class="footer"><svg viewBox="0 0 264 38" preserveAspectRatio="none"><path d="M0 22 C70 8 150 30 264 12 L264 38 L0 38Z" fill="var(--band)"/><path d="M0 20 C70 6 150 28 264 10" fill="none" stroke="var(--band-line)" stroke-width="2.4"/><path d="M0 16 C80 4 160 22 264 6" fill="none" stroke="#cfcfcf" stroke-width=".6"/></svg><span class="footer-url">www.kestreleg.com.au</span></div>
</section>

<!-- Content -->
<section class="slide row-bottom col-3">
  <h2 class="slide-heading">Lorem Ipsum</h2>
  <p class="copy" style="left:24px;top:36px;width:228px">Orem ipsum dolor sit amet, consectetuer adipiscing elit, sed diam nonummy nibh euismod tincidunt ut laoreet dolore magna aliquam erat volutpat. Ut wisi enim ad minim veniam, quis nostrud exerci tation ullamcorper suscipit lobortis nisl ut aliquip ex ea commodo consequat.</p>
  <div class="photo" style="left:22px;top:88px;width:86px;height:74px;background:linear-gradient(180deg,#c9302c 0%,#d8d0c8 45%,#8a7a6a 100%)" role="img" aria-label="Family in front of a model house with a red roof"></div>
  <div class="photo" style="left:128px;top:88px;width:84px;height:74px;background:linear-gradient(135deg,#f4f1ee,#d9b8a0 55%,#b08a70)" role="img" aria-label="Smiling woman holding a card"></div>
  <div class="footer"><svg viewBox="0 0 264 38" preserveAspectRatio="none"><path d="M0 22 C70 8 150 30 264 12 L264 38 L0 38Z" fill="var(--band)"/><path d="M0 20 C70 6 150 28 264 10" fill="none" stroke="var(--band-line)" stroke-width="2.4"/><path d="M0 16 C80 4 160 22 264 6" fill="none" stroke="#cfcfcf" stroke-width=".6"/></svg><span class="footer-url">www.kestreleg.com.au</span></div>
</section>

<!-- Closing -->
<section class="slide row-bottom col-4">
  <div class="brand" style="left:40px;top:50px"><span class="brand-mark"></span>Kestrel Estate Group</div>
  <p class="thanks">THANK YOU<br>FOR ATTENTION</p>
  <div class="footer"><svg viewBox="0 0 264 38" preserveAspectRatio="none"><path d="M0 22 C70 8 150 30 264 12 L264 38 L0 38Z" fill="var(--band)"/><path d="M0 20 C70 6 150 28 264 10" fill="none" stroke="var(--band-line)" stroke-width="2.4"/><path d="M0 16 C80 4 160 22 264 6" fill="none" stroke="#cfcfcf" stroke-width=".6"/></svg><span class="footer-url">www.kestreleg.com.au</span></div>
</section>

</body>
</html>
```